Karriernet Banner Design (Profilbanner und Unternehmensbanner) (1584 x 396) (1128 x 191)
Zielgruppe
Ich bin Dienstleister und Unternehmensberater für technischen B2B Vertrieb.
Für meinen KarrierNet Account suche ich einen Banner für meine Profilseite und einen Banner für die Unternehmensseite). Meine Zielgruppe sind leitende Angestellte in Unternehmen. Das Design sollte entsprechend grafisch hochwertig, seriös gestaltet sein.
I am a service provider and management consultant for technical B2B sales.
For my KarrierNet account, I'm looking for a banner for my profile page and a banner for the company page). My target group are executives in companies. The design should have a correspondingly high-quality graphic design and be serious.
Aufgabenstellung
Wichtig ist die Berücksichtigung meines Logos (PNG im Anhang) und des Corporate Identity Farben (PDF Anhang und unten stehend). Stock Bilder oder Grafiken können/sollen gerne mit eingebunden werden. Wichtig ist hier der passende Gesamteindruck.
It is important to consider my logo (PNG in the attachment) and the corporate identity colors (PDF attachment and below). Stock images or graphics can/should be included. The right overall impression is important here.
HEX / HTML 002854
HEX / HTML 00b6e3
Bannergrößen / Banner sizes
Profilbanner (1584 x 396)
Unternehmensseitenbanner (1128 x 191)

```html
<!DOCTYPE html>
<html lang="de">
<head>
<meta charset="utf-8">
<title>Matthias Kernow Management &amp; Sales Consulting GmbH – KarrierNet Unternehmensseite</title>
<link rel="stylesheet" href="https://fonts.googleapis.com/css2?family=Titillium+Web:wght@300;400;600;700&family=Source+Sans+3:wght@400;600&display=swap">
<style>
  :root {
    --navy: #002854;
    --navy-deep: #041a38;
    --cyan: #00b6e3;
    --white: #ffffff;
    --ink: #1f1f1f;
    --ink-soft: #3a3a3a;
    --muted: #6b6b6b;
    --action: #0a66c2;
    --rule: #e6e6e6;
  }
  * { margin: 0; padding: 0; box-sizing: border-box; }
  html, body { width: 1200px; height: 656px; overflow: hidden; background: var(--white); }
  .page { position: relative; width: 1200px; height: 656px; font-family: "Source Sans 3", sans-serif; }

  .banner {
    position: absolute; left: 0; top: 0; width: 1200px; height: 299px;
    background: linear-gradient(100deg, #0a4f9a 0%, #063a78 25%, var(--navy) 55%, var(--navy-deep) 100%);
    overflow: hidden; font-family: "Titillium Web", sans-serif; color: var(--white);
  }
  .banner-waves {
    position: absolute; left: 0; top: 0; width: 640px; height: 240px;
    background: radial-gradient(ellipse at 20% 20%, rgba(0,182,227,0.55), rgba(0,182,227,0.15) 45%, transparent 70%);
  }
  .banner-engine {
    position: absolute; left: 712px; top: 0; width: 488px; height: 299px;
    background: radial-gradient(ellipse at 40% 55%, #9aa3ad 0%, #4a5058 30%, #1b1e23 65%, #0c0e12 100%);
  }
  .headline { position: absolute; left: 201px; top: 66px; font-size: 36px; line-height: 1; letter-spacing: 0.2px; }
  .headline .line-two { display: block; margin-left: 38px; margin-top: 17px; }
  .headline .light { font-weight: 300; font-size: 31px; }
  .headline .bold { font-weight: 700; }
  .contact { position: absolute; top: 250px; left: 239px; display: flex; align-items: center; gap: 20px; font-size: 15px; font-weight: 600; }
  .contact-item { display: flex; align-items: center; gap: 8px; }
  .contact svg { width: 23px; height: 23px; }

  .company-mark {
    position: absolute; left: 38px; top: 210px; width: 168px; height: 164px;
    background: #13284a; border: 2px solid var(--white);
    display: flex; align-items: center; justify-content: center;
    font-family: "Titillium Web", sans-serif; font-weight: 600; font-size: 30px; color: var(--cyan);
  }

  .company-name { position: absolute; left: 35px; top: 396px; font-size: 35px; font-weight: 600; color: var(--ink); letter-spacing: 0.1px; }
  .tagline { position: absolute; left: 35px; top: 444px; font-size: 22px; color: var(--ink-soft); }
  .meta { position: absolute; left: 34px; top: 477px; font-size: 19px; color: var(--muted); }
  .staff-link { position: absolute; left: 35px; top: 521px; font-size: 22px; font-weight: 600; color: var(--muted); }

  .actions { position: absolute; left: 35px; top: 579px; display: flex; gap: 13px; }
  .btn {
    height: 49px; border-radius: 25px; font-size: 23px; font-weight: 600;
    display: flex; align-items: center; justify-content: center; gap: 10px;
  }
  .btn-follow { width: 210px; background: var(--action); color: var(--white); }
  .btn-site { width: 292px; border: 2px solid var(--action); color: var(--action); }
  .btn-more { width: 110px; border: 2px solid #8c8c8c; color: #5e5e5e; font-weight: 400; }
  .btn svg { width: 20px; height: 20px; }
  .page-rule { position: absolute; left: 0; top: 652px; width: 1200px; height: 2px; background: var(--rule); }
</style>
</head>
<body>
<div class="page">
  <section class="banner">
    <div class="banner-waves" role="img" aria-label="Abstrakte blaue Linienwellen"></div>
    <div class="banner-engine" role="img" aria-label="Foto eines Automotors mit Riemenscheiben"></div>
    <h1 class="headline">
      <span class="light">VOLLE</span> <span class="bold">POWER</span>
      <span class="line-two"><span class="light">FÜR IHR</span> <span class="bold">BUSINESS</span><span class="light">.</span></span>
    </h1>
    <div class="contact">
      <span class="contact-item">
        <svg viewBox="0 0 24 24" fill="none" stroke="currentColor" stroke-width="1.6" stroke-linejoin="round"><path d="M5 3h4l2 5-3 2a12 12 0 0 0 6 6l2-3 5 2v4a2 2 0 0 1-2 2A18 18 0 0 1 3 5a2 2 0 0 1 2-2z"/></svg>
        0987 | 654 321 0
      </span>
      <span class="contact-item">
        <svg viewBox="0 0 24 24" fill="none" stroke="currentColor" stroke-width="1.5"><circle cx="12" cy="12" r="10"/><ellipse cx="12" cy="12" rx="4.5" ry="10"/><path d="M2 12h20M4 6.5h16M4 17.5h16"/></svg>
        MATTHIASKERNOW.DE
      </span>
    </div>
  </section>

  <div class="company-mark">Kernow</div>

  <h2 class="company-name">Matthias Kernow Management &amp; Sales Consulting GmbH</h2>
  <p class="tagline">B2B Sales Consulting</p>
  <p class="meta">Business Consulting und Unternehmensdienstleistungen · Bad Lindental, North Rhine-Westphalia · 1 Follower</p>
  <p class="staff-link">1 Mitarbeiter:in auf KarrierNet ansehen</p>

  <div class="actions">
    <span class="btn btn-follow">
      <svg viewBox="0 0 20 20" stroke="currentColor" stroke-width="2.6"><path d="M10 2v16M2 10h16"/></svg>
      Folgen
    </span>
    <span class="btn btn-site">
      Website besuchen
      <svg viewBox="0 0 20 20" fill="none" stroke="currentColor" stroke-width="2.4"><path d="M9 4H4v12h12v-5M11 2h7v7M18 2l-9 9"/></svg>
    </span>
    <span class="btn btn-more">Mehr</span>
  </div>
  <div class="page-rule"></div>
</div>
</body>
</html>
```